Recruiting ad for Caregivers and Nurses

We need a few amazing, fun, catchy, creative recruiting ads for Caregivers and Nurses to care for homecare patients on the island of Oahu, in Hawaii. We are an in home care company called Brantley Homecare. Our care services are provided 24/7, so we need staff that can work days, nights, weekdays, weekends. We need catchy fun ads to entice caregivers and nurses to call our office to inquire about jobs available. Our patients age range is from babies to seniors. We need caregivers and nurses for basic patient care (bathing, dressing, ambulating, preparing meals, medication reminders, light housekeeping) and complex patients (oxygen, tube feeding, injections, vents, wound care). Here are some bullets to consider including:
*Full-time and Part-time Positions Available (days, nights, weekdays, weekends)
*Sign-On Bonus Programs Offered up to $500
*Refer a Friend Bonus Program
*Holiday Pay
*2 Health Plans to Choose from
*Island-Wide Locations
*All PPE Provided (masks, gloves, etc)
*401K Program
*Tuition Benefits

```html
<!DOCTYPE html>
<html lang="en">
<head>
<meta charset="utf-8">
<title>Brantley Homecare – Caregivers and Nurses Recruiting Flyer</title>
<link rel="stylesheet" href="https://fonts.googleapis.com/css2?family=Marcellus&family=Great+Vibes&family=Arimo:wght@400;700&display=swap">
<style>
  :root {
    --backdrop: #9d9ba3;
    --paper: #ffffff;
    --mint: #a6dcd5;
    --mint-light: #e9f6f4;
    --coral: #f39a80;
    --coral-deep: #ee8a6c;
    --forest: #1f5a4c;
    --slate: #3f6571;
    --slate-dark: #2f4f5a;
    --ink-light: #ffffff;
  }
  * { margin: 0; padding: 0; box-sizing: border-box; }
  html, body {
    width: 1200px; height: 1200px; overflow: hidden;
    background: var(--backdrop);
  }
  .flyer {
    position: absolute; left: 226px; top: 116px;
    width: 624px; height: 807px;
    transform: scale(1.2); transform-origin: 0 0;
    background: var(--paper); overflow: hidden;
    font-family: "Arimo", Arial, sans-serif;
  }
  .flyer-shapes { position: absolute; inset: 0; width: 624px; height: 807px; }
  .headline {
    position: absolute; left: 0; right: 20px; top: 14px;
    font-family: "Marcellus", Georgia, serif; font-weight: 400; color: var(--forest);
    text-align: right; line-height: 1;
  }
  .headline-line1 { display: block; font-size: 48px; margin-right: 176px; }
  .headline-line2 { display: block; font-size: 48px; margin-top: 4px; }
  .headline-and {
    font-family: "Great Vibes", cursive; color: var(--coral);
    font-size: 46px; margin-right: 12px;
  }
  .brand-badge {
    position: absolute; left: 418px; top: 348px; width: 188px; height: 188px;
    border-radius: 50%; background: var(--paper);
    border: 3px solid var(--coral);
    box-shadow: 0 0 0 5px var(--paper);
    display: flex; flex-direction: column; align-items: center; justify-content: center;
    font-family: "Marcellus", Georgia, serif; color: var(--forest);
    font-size: 30px; line-height: 1.05; text-align: center;
  }
  .role-icon {
    position: absolute; left: 18px; top: 408px; width: 48px; height: 48px;
    border: 2px solid var(--slate); border-radius: 50%;
  }
  .positions { position: absolute; left: 18px; top: 470px; font-weight: 700; }
  .positions-type { color: var(--coral-deep); font-size: 19px; letter-spacing: .2px; }
  .positions-title { color: var(--forest); font-size: 21px; margin-top: 2px; letter-spacing: .3px; }
  .shift-pill {
    position: absolute; left: 16px; top: 521px; width: 268px; height: 23px;
    border-radius: 12px; background: var(--coral);
    color: var(--ink-light); font-size: 13.5px; line-height: 23px; text-align: center;
  }
  .benefits {
    position: absolute; left: 104px; width: 400px; top: 553px;
    list-style: none; text-align: center; color: var(--forest);
    font-size: 12.6px; line-height: 16.4px;
  }
  .benefits li::before {
    content: ""; display: inline-block; width: 7px; height: 7px; border-radius: 50%;
    background: var(--coral); margin-right: 6px; vertical-align: 1px;
  }
  .benefits strong { font-weight: 700; }
  .care-types {
    position: absolute; left: 12px; top: 704px; width: 300px;
    list-style: none; color: var(--ink-light); font-size: 11.2px; line-height: 13.6px;
  }
  .care-types li::before {
    content: ""; display: inline-block; width: 6px; height: 6px; border-radius: 50%;
    background: var(--coral); margin-right: 5px; vertical-align: 1px;
  }
  .care-types strong { color: var(--coral); font-weight: 700; }
  .care-types span { display: block; padding-left: 12px; }
  .call-label {
    position: absolute; right: 20px; top: 716px;
    font-family: "Marcellus", Georgia, serif; color: var(--slate-dark); font-size: 27px;
  }
  .phone {
    position: absolute; right: 18px; top: 752px;
    display: flex; align-items: center; gap: 8px;
    color: var(--ink-light); font-size: 29px;
  }
  .phone-icon { width: 27px; height: 27px; }
</style>
</head>
<body>
<main class="flyer">
  <svg class="flyer-shapes" viewBox="0 0 624 807">
    <defs>
      <linearGradient id="photoTone" x1="0" y1="0" x2="1" y2="1">
        <stop offset="0" stop-color="#e4d79e"/>
        <stop offset=".45" stop-color="#c8a47c"/>
        <stop offset=".75" stop-color="#7ea8b8"/>
        <stop offset="1" stop-color="#8c9a70"/>
      </linearGradient>
      <linearGradient id="headerTone" x1="0" y1="0" x2="1" y2="0">
        <stop offset="0" stop-color="#d9f0ec"/>
        <stop offset=".45" stop-color="#ffffff"/>
        <stop offset="1" stop-color="#a6dcd5"/>
      </linearGradient>
    </defs>
    <rect class="photo-area" x="0" y="0" width="624" height="560" fill="url(#photoTone)"
          role="img" aria-label="Photo: a smiling caregiver in blue scrubs sits on a sofa beside a patient in a bright living room"/>
    <path class="header-accent" fill="var(--coral)"
          d="M0,0 H624 V255 C560,225 470,196 380,178 C260,152 150,118 60,62 C38,48 18,38 0,34 Z"/>
    <path class="header-band" fill="url(#headerTone)"
          d="M40,0 H624 V232 C560,200 470,172 380,154 C260,130 170,92 100,36 C80,20 60,8 40,0 Z"/>
    <path class="body-accent" fill="var(--mint)"
          d="M0,306 C150,380 350,440 624,520 V560 C360,490 150,420 0,340 Z"/>
    <path class="body-panel" fill="var(--paper)"
          d="M0,322 C150,400 350,462 624,540 V807 H0 Z"/>
    <path class="footer-panel" fill="var(--slate)"
          d="M0,698 H300 C420,698 520,672 624,612 V807 H0 Z"/>
    <path class="footer-swoosh" fill="var(--mint)"
          d="M310,807 C390,720 505,672 624,638 V668 C525,696 445,744 405,807 Z"/>
    <path class="footer-call" fill="var(--coral)"
          d="M355,807 C425,738 522,696 624,668 V807 Z"/>
    <rect class="footer-strip" x="0" y="797" width="624" height="10" fill="var(--slate)"/>
  </svg>

  <h1 class="headline">
    <span class="headline-line1">Caregivers</span>
    <span class="headline-line2"><span class="headline-and">and</span> Nurses</span>
  </h1>

  <div class="brand-badge">Brantley<br>Homecare</div>

  <div class="role-icon" aria-hidden="true"></div>

  <div class="positions">
    <div class="positions-type">FULL-TIME &amp; PART-TIME</div>
    <div class="positions-title">POSITIONS AVAILABLE</div>
  </div>
  <div class="shift-pill">(Days, Nights, Weekdays, Weekends)</div>

  <ul class="benefits">
    <li><strong>SIGN-ON BONUS PROGRAMS -</strong> Offered up to $500</li>
    <li><strong>REFER A FRIEND BONUS PROGRAM</strong></li>
    <li><strong>HOLIDAY PAY</strong></li>
    <li><strong>2 HEALTH PLANS</strong> to choose from</li>
    <li>Island-Wide Locations</li>
    <li><strong>All PPE Provided</strong> (Masks, gloves, etc)</li>
    <li><strong>401K PROGRAM</strong></li>
    <li><strong>TUITION BENEFITS</strong></li>
  </ul>

  <ul class="care-types">
    <li><strong>BABIES TO SENIORS</strong></li>
    <li><strong>BASIC PATIENT CARE</strong>
      <span>(bathing, dressing, ambulating, preparing meals, medication reminders, light housekeeping)</span></li>
    <li><strong>COMPLEX PATIENTS</strong>
      <span>(oxygen, tube feeding, injections, vents, wound care).</span></li>
  </ul>

  <div class="call-label">Call Us</div>
  <div class="phone">
    <svg class="phone-icon" viewBox="0 0 24 24" aria-hidden="true">
      <circle cx="12" cy="12" r="12" fill="var(--slate-dark)"/>
      <path fill="var(--ink-light)" d="M9 6.5c.4 0 .7.3.8.6l.6 1.8c.1.3 0 .7-.3.9l-.9.7c.6 1.3 1.6 2.3 2.9 2.9l.7-.9c.2-.3.6-.4.9-.3l1.8.6c.3.1.6.4.6.8v1.6c0 .5-.4.9-.9.9C10 16 8 14 8 7.4c0-.5.4-.9.9-.9z"/>
    </svg>
    <span>808-555-0147</span>
  </div>
</main>
</body>
</html>
```